Beer Can Label design - MISTLY ALE

Mistly Ale. (Acronym for New England India Pale Ale)
Full sleeve (473ml)
5.00" x 8.125" Inches
Write up on can reverse.
Opaque haze in appearance derived from specific oats, wheat, and water chemistry. This brew bolsters a dense and creamy head, leaving behind a soft and silky mouth-feel. Expect an intense tropical fruit centric aroma and flavour. Our timely hop additions contributes to less bitterness than typical IPA’s.
Logo is to be on front, towards bottom. Title near top.
Looking for something that stands out. Bold.
Target Market(s)
Craft beer enthusiasts
Industry/Entity Type
Beer & Brewing
Requirements
Must have
- Eye catching.

```html
<!DOCTYPE html>
<html lang="en">
<head>
<meta charset="utf-8">
<title>Mistly Ale – Alternate Label Options</title>
<link rel="stylesheet" href="https://fonts.googleapis.com/css2?family=Poiret+One&family=Montserrat:wght@500;700&display=swap">
<style>
  :root {
    --page-bg: #f6f7fa;
    --white: #ffffff;
    --teal: #13937f;
    --teal-light: #3dbb9c;
    --lime: #8dc63f;
    --lime-soft: #c7e36a;
    --ink: #0f1c24;
    --caption-ink: #4a4a52;
  }
  * { box-sizing: border-box; margin: 0; padding: 0; }
  html, body { width: 1200px; height: 402px; overflow: hidden; background: var(--page-bg); }
  .board { position: relative; width: 1200px; height: 402px; }

  .label { position: absolute; top: 70px; width: 216px; height: 252px; overflow: visible;
           filter: drop-shadow(3px 5px 5px rgba(0,0,0,.16)); }
  .label--white { left: 180px; }
  .label--teal  { left: 492px; }
  .label--lime  { left: 804px; }

  .label--white { --bg: var(--white); --frame: var(--teal-light); --ring-text: var(--teal-light); --name: var(--lime); --rule: var(--teal-light); --hop-bg: #eceeec; --hop: var(--lime); }
  .label--teal  { --bg: var(--teal); --frame: var(--lime-soft); --ring-text: var(--white); --name: var(--white); --rule: var(--lime-soft); --hop-bg: #1a8a78; --hop: var(--lime); }
  .label--lime  { --bg: var(--lime); --frame: var(--ink); --ring-text: var(--white); --name: var(--ink); --rule: var(--ink); --hop-bg: #82b93a; --hop: #3f6e1e; }

  .label__shape { fill: var(--bg); }
  .label__frame { fill: none; stroke: var(--frame); stroke-width: .8; stroke-dasharray: 6 2 1 2; }
  .label__ring  { fill: none; stroke: var(--frame); stroke-width: .8; stroke-dasharray: 5 2 1 2; }
  .label__corner { fill: var(--lime-soft); }
  .label__ring-text { font-family: "Poiret One", sans-serif; font-size: 9px; letter-spacing: 3px; fill: var(--ring-text); font-weight: 700; }
  .label__name { font-family: "Montserrat", sans-serif; font-weight: 700; fill: var(--name); }
  .label__name--main { font-size: 42px; }
  .label__name--sub { font-size: 30px; }
  .label__rule { stroke: var(--rule); stroke-width: .8; stroke-dasharray: 4 2; }
  .label__hop-art { fill: var(--hop-bg); opacity: .8; }
  .label__hop-icon { fill: var(--hop); }

  .caption { position: absolute; left: 0; top: 374px; height: 18px; width: 215px; display: flex;
             border: 1px solid var(--caption-ink); border-left: none; }
  .caption__tab { width: 18px; background: var(--caption-ink); }
  .caption__text { font-family: "Montserrat", sans-serif; font-weight: 500; font-size: 9.5px; letter-spacing: .6px;
                   color: var(--caption-ink); line-height: 16px; padding-left: 18px; }
</style>
</head>
<body>
<main class="board">

  <svg class="label label--white" viewBox="0 0 216 252" aria-label="White label option">
    <path class="label__shape" d="M18,10 Q108,-6 198,10 Q214,12 212,28 Q204,126 212,224 Q214,240 198,242 Q108,258 18,242 Q2,240 4,224 Q12,126 4,28 Q2,12 18,10Z"/>
    <path class="label__frame" d="M22,18 Q108,4 194,18 L200,24 Q194,126 200,228 L194,234 Q108,248 22,234 L16,228 Q22,126 16,24Z"/>
    <circle class="label__ring" cx="108" cy="126" r="96"/>
    <ellipse class="label__hop-art" role="img" aria-label="Faint hop cone and leaves illustration" cx="108" cy="130" rx="62" ry="80"/>
    <path id="arcTopW" d="M28,126 A80,80 0 0 1 188,126" fill="none"/>
    <path id="arcBotW" d="M20,126 A88,88 0 0 0 196,126" fill="none"/>
    <text class="label__ring-text"><textPath href="#arcTopW" startOffset="50%" text-anchor="middle">NEW ENGLAND INDIAN PALE ALE</textPath></text>
    <text class="label__ring-text"><textPath href="#arcBotW" startOffset="50%" text-anchor="middle">BREWED FOR BOLD PALATES</textPath></text>
    <ellipse class="label__hop-icon" role="img" aria-label="Hop cone icon" cx="22" cy="126" rx="7" ry="9"/>
    <ellipse class="label__hop-icon" role="img" aria-label="Hop cone icon" cx="194" cy="126" rx="7" ry="9"/>
    <line class="label__rule" x1="120" y1="86" x2="162" y2="86"/>
    <line class="label__rule" x1="140" y1="164" x2="170" y2="164"/>
    <line class="label__rule" x1="140" y1="170" x2="170" y2="170"/>
    <line class="label__rule" x1="56" y1="180" x2="162" y2="180"/>
    <text class="label__name label__name--main" x="108" y="136" text-anchor="middle">Mistly</text>
    <text class="label__name label__name--sub" x="104" y="170" text-anchor="middle">Ale</text>
  </svg>

  <svg class="label label--teal" viewBox="0 0 216 252" aria-label="Teal label option">
    <path class="label__shape" d="M18,10 Q108,-6 198,10 Q214,12 212,28 Q204,126 212,224 Q214,240 198,242 Q108,258 18,242 Q2,240 4,224 Q12,126 4,28 Q2,12 18,10Z"/>
    <path class="label__corner" d="M16,16 L32,16 L16,32Z M200,16 L184,16 L200,32Z M16,236 L32,236 L16,220Z M200,236 L184,236 L200,220Z"/>
    <circle class="label__ring" cx="108" cy="126" r="96"/>
    <ellipse class="label__hop-art" role="img" aria-label="Faint hop cone and leaves illustration" cx="108" cy="130" rx="62" ry="80"/>
    <path id="arcTopT" d="M28,126 A80,80 0 0 1 188,126" fill="none"/>
    <path id="arcBotT" d="M20,126 A88,88 0 0 0 196,126" fill="none"/>
    <text class="label__ring-text"><textPath href="#arcTopT" startOffset="50%" text-anchor="middle">NEW ENGLAND INDIAN PALE ALE</textPath></text>
    <text class="label__ring-text"><textPath href="#arcBotT" startOffset="50%" text-anchor="middle">BREWED FOR BOLD PALATES</textPath></text>
    <ellipse class="label__hop-icon" role="img" aria-label="Hop cone icon" cx="22" cy="126" rx="7" ry="9"/>
    <ellipse class="label__hop-icon" role="img" aria-label="Hop cone icon" cx="194" cy="126" rx="7" ry="9"/>
    <line class="label__rule" x1="120" y1="86" x2="162" y2="86"/>
    <line class="label__rule" x1="140" y1="164" x2="170" y2="164"/>
    <line class="label__rule" x1="140" y1="170" x2="170" y2="170"/>
    <line class="label__rule" x1="56" y1="180" x2="162" y2="180"/>
    <text class="label__name label__name--main" x="108" y="136" text-anchor="middle">Mistly</text>
    <text class="label__name label__name--sub" x="104" y="170" text-anchor="middle">Ale</text>
  </svg>

  <svg class="label label--lime" viewBox="0 0 216 252" aria-label="Lime label option">
    <path class="label__shape" d="M18,10 Q108,-6 198,10 Q214,12 212,28 Q204,126 212,224 Q214,240 198,242 Q108,258 18,242 Q2,240 4,224 Q12,126 4,28 Q2,12 18,10Z"/>
    <path class="label__frame" d="M22,18 Q108,4 194,18 L200,24 Q194,126 200,228 L194,234 Q108,248 22,234 L16,228 Q22,126 16,24Z"/>
    <circle class="label__ring" cx="108" cy="126" r="96"/>
    <ellipse class="label__hop-art" role="img" aria-label="Faint hop cone and leaves illustration" cx="108" cy="130" rx="62" ry="80"/>
    <path id="arcTopL" d="M28,126 A80,80 0 0 1 188,126" fill="none"/>
    <path id="arcBotL" d="M20,126 A88,88 0 0 0 196,126" fill="none"/>
    <text class="label__ring-text"><textPath href="#arcTopL" startOffset="50%" text-anchor="middle">NEW ENGLAND INDIAN PALE ALE</textPath></text>
    <text class="label__ring-text"><textPath href="#arcBotL" startOffset="50%" text-anchor="middle">BREWED FOR BOLD PALATES</textPath></text>
    <ellipse class="label__hop-icon" role="img" aria-label="Hop cone icon" cx="22" cy="126" rx="7" ry="9"/>
    <ellipse class="label__hop-icon" role="img" aria-label="Hop cone icon" cx="194" cy="126" rx="7" ry="9"/>
    <line class="label__rule" x1="120" y1="86" x2="162" y2="86"/>
    <line class="label__rule" x1="140" y1="164" x2="170" y2="164"/>
    <line class="label__rule" x1="140" y1="170" x2="170" y2="170"/>
    <line class="label__rule" x1="56" y1="180" x2="162" y2="180"/>
    <text class="label__name label__name--main" x="108" y="136" text-anchor="middle">Mistly</text>
    <text class="label__name label__name--sub" x="104" y="170" text-anchor="middle">Ale</text>
  </svg>

  <div class="caption">
    <span class="caption__tab"></span>
    <span class="caption__text">ALTERNATE LABEL OPTIONS</span>
  </div>

</main>
</body>
</html>
```